Electrical business needs a flyer design

we need a Trifold flyer designed for an electrical company. Our service include new installations, renovations and rewires, safety checks, switchboard upgrades, services and breakdown, home automation and power monitoring. we would like to see designs using dark grey, orange and blue. the final designs should communicate a friendly but professional service. I have attached my old business brochure to indicate the service we provide
Target Market(s)
home owners
Industry/Entity Type
Electrical
Look and feel
Each slider illustrates characteristics of the customer's brand and the style your logo design should communicate.

```html
<!DOCTYPE html>
<html lang="en">
<head>
<meta charset="utf-8">
<title>Volta Line Electrical – Trifold</title>
<link href="https://fonts.googleapis.com/css2?family=Montserrat:wght@400;500;600;700;800&display=swap" rel="stylesheet">
<style>
:root{
  --blue:#1787d6;
  --blue-dark:#0f5fb0;
  --orange:#f07a22;
  --orange-deep:#e85a14;
  --grey-text:#3a3a3a;
  --grey-dark:#2b2b2b;
  --paper:#f4f5f6;
  --paper-shade:#e6e8ea;
  --white:#ffffff;
}
*{box-sizing:border-box;margin:0;padding:0}
html,body{width:1200px;height:800px;overflow:hidden;background:#ececec}
body{font-family:"Montserrat",Arial,sans-serif;color:var(--grey-text)}
.trifold{position:relative;width:1200px;height:800px;display:flex}
.panel{position:relative;width:400px;height:800px;overflow:hidden;
  background:linear-gradient(160deg,var(--white) 0%,var(--paper) 45%,var(--paper-shade) 100%)}
.band-top,.band-bottom{position:absolute;left:0;width:400px}
.band-top{top:0;height:90px}
.band-bottom{bottom:0;height:170px}
.heading{position:absolute;left:44px;top:100px}
.heading .light{display:block;font-weight:400;font-size:34px;letter-spacing:1px;color:var(--grey-dark);text-transform:uppercase}
.heading .bold{display:block;font-weight:800;font-size:34px;color:var(--orange);text-transform:uppercase;margin-top:-4px}
.rule{position:absolute;left:44px;width:320px;height:2px;background:var(--blue)}
.service-list{position:absolute;left:44px;list-style:none}
.service-list li{display:flex;align-items:flex-start;gap:12px;font-weight:600;font-size:18px;color:var(--grey-dark);line-height:1.2;margin-bottom:13px}
.service-list svg{flex:none;width:20px;height:20px;margin-top:1px}
.photo{position:absolute}
.panel-electrical .rule{top:190px}
.panel-electrical .service-list{top:210px}
.panel-electrical .photo{left:0;top:440px;width:400px;height:260px;
  background:linear-gradient(150deg,#e9e2d6 0%,#c9c2b6 40%,#2d3c50 70%,#1c2634 100%)}
.panel-communication .heading .light{font-size:31px}
.panel-communication .rule{top:190px}
.panel-communication .service-list{top:210px}
.panel-communication .photo{left:0;top:440px;width:400px;height:260px;
  background:linear-gradient(160deg,#f2f3f5 0%,#dfe3e8 40%,#2f6db8 75%,#23549a 100%)}
.panel-philosophy .heading{top:80px}
.panel-philosophy .heading .light{display:inline;font-size:30px}
.panel-philosophy .heading .bold{display:inline;font-size:30px}
.panel-philosophy .rule{top:125px}
.philosophy-text{position:absolute;left:44px;top:140px;width:320px;font-size:13px;line-height:1.55;color:var(--grey-text)}
.panel-philosophy .photo{left:60px;top:290px;width:340px;height:200px;
  background:linear-gradient(135deg,#efe9e4 0%,#d9c8bb 45%,#e6c75a 70%,#cfd3d6 100%)}
.cta-block{position:absolute;left:0;top:430px;width:400px;height:370px}
.cta-text{position:absolute;left:40px;top:540px;width:330px;text-align:center;font-weight:800;font-size:27px;line-height:1.25;color:var(--white);text-transform:uppercase}
.cta-text .highlight{display:inline-block;background:var(--orange);padding:0 8px}
.phone-pill{position:absolute;left:36px;top:700px;width:330px;height:54px;border-radius:27px;background:var(--white);
  display:flex;align-items:center;gap:12px;padding-left:10px}
.phone-pill svg{width:40px;height:40px}
.phone-pill span{font-weight:800;font-size:28px;color:var(--orange);letter-spacing:1px}
.emergency{position:absolute;left:240px;top:742px;display:flex;align-items:center;gap:10px;z-index:5}
.emergency .dot{width:14px;height:14px;border-radius:50%;background:var(--white)}
.emergency .label{font-weight:800;font-size:20px;color:var(--white);text-transform:uppercase;letter-spacing:1px;white-space:nowrap}
</style>
</head>
<body>
<main class="trifold">

  <section class="panel panel-electrical">
    <svg class="band-top" viewBox="0 0 400 90" preserveAspectRatio="none">
      <path d="M0 0H400V55C300 20 180 20 0 45Z" fill="var(--blue)"/>
      <path d="M230 26C310 22 370 35 400 55V90C360 55 300 35 230 26Z" fill="var(--orange-deep)"/>
    </svg>
    <h2 class="heading"><span class="light">Electrical</span><span class="bold">Service</span></h2>
    <div class="rule"></div>
    <ul class="service-list">
      <li><svg viewBox="0 0 20 20"><circle cx="10" cy="10" r="8.5" fill="none" stroke="var(--orange)" stroke-width="1.6"/><path d="M6 10.3l2.6 2.5L14 7.5" fill="none" stroke="var(--orange)" stroke-width="1.8"/></svg>New Installation</li>
      <li><svg viewBox="0 0 20 20"><circle cx="10" cy="10" r="8.5" fill="none" stroke="var(--orange)" stroke-width="1.6"/><path d="M6 10.3l2.6 2.5L14 7.5" fill="none" stroke="var(--orange)" stroke-width="1.8"/></svg>Renovations And Re-wiring</li>
      <li><svg viewBox="0 0 20 20"><circle cx="10" cy="10" r="8.5" fill="none" stroke="var(--orange)" stroke-width="1.6"/><path d="M6 10.3l2.6 2.5L14 7.5" fill="none" stroke="var(--orange)" stroke-width="1.8"/></svg>Installation Of Safety Switches</li>
      <li><svg viewBox="0 0 20 20"><circle cx="10" cy="10" r="8.5" fill="none" stroke="var(--orange)" stroke-width="1.6"/><path d="M6 10.3l2.6 2.5L14 7.5" fill="none" stroke="var(--orange)" stroke-width="1.8"/></svg>Switchboard Upgrades</li>
      <li><svg viewBox="0 0 20 20"><circle cx="10" cy="10" r="8.5" fill="none" stroke="var(--orange)" stroke-width="1.6"/><path d="M6 10.3l2.6 2.5L14 7.5" fill="none" stroke="var(--orange)" stroke-width="1.8"/></svg>Services And Break Downs</li>
      <li><svg viewBox="0 0 20 20"><circle cx="10" cy="10" r="8.5" fill="none" stroke="var(--orange)" stroke-width="1.6"/><path d="M6 10.3l2.6 2.5L14 7.5" fill="none" stroke="var(--orange)" stroke-width="1.8"/></svg>Home Automation</li>
    </ul>
    <div class="photo" role="img" aria-label="Photo of hands holding a tablet showing a home control app in a bright living room"></div>
    <svg class="band-bottom" viewBox="0 0 400 170" preserveAspectRatio="none">
      <path d="M0 20C50 70 110 90 170 90L0 150Z" fill="var(--blue)"/>
      <path d="M0 120C140 150 270 90 400 30V170H0Z" fill="var(--orange)"/>
    </svg>
  </section>

  <section class="panel panel-communication">
    <svg class="band-top" viewBox="0 0 400 90" preserveAspectRatio="none">
      <path d="M0 0H400V20C300 30 150 20 0 60Z" fill="var(--orange)"/>
      <path d="M300 22C350 18 380 20 400 24V0H300Z" fill="var(--blue)"/>
    </svg>
    <h2 class="heading"><span class="light">Communication</span><span class="bold">Service</span></h2>
    <div class="rule"></div>
    <ul class="service-list">
      <li><svg viewBox="0 0 20 20"><circle cx="10" cy="10" r="8.5" fill="none" stroke="var(--orange)" stroke-width="1.6"/><path d="M6 10.3l2.6 2.5L14 7.5" fill="none" stroke="var(--orange)" stroke-width="1.8"/></svg>New Installation</li>
      <li><svg viewBox="0 0 20 20"><circle cx="10" cy="10" r="8.5" fill="none" stroke="var(--orange)" stroke-width="1.6"/><path d="M6 10.3l2.6 2.5L14 7.5" fill="none" stroke="var(--orange)" stroke-width="1.8"/></svg>Additional Phone and<br>Data Points</li>
      <li><svg viewBox="0 0 20 20"><circle cx="10" cy="10" r="8.5" fill="none" stroke="var(--orange)" stroke-width="1.6"/><path d="M6 10.3l2.6 2.5L14 7.5" fill="none" stroke="var(--orange)" stroke-width="1.8"/></svg>Antennas And Tv Points</li>
      <li><svg viewBox="0 0 20 20"><circle cx="10" cy="10" r="8.5" fill="none" stroke="var(--orange)" stroke-width="1.6"/><path d="M6 10.3l2.6 2.5L14 7.5" fill="none" stroke="var(--orange)" stroke-width="1.8"/></svg>LAN Setup</li>
      <li><svg viewBox="0 0 20 20"><circle cx="10" cy="10" r="8.5" fill="none" stroke="var(--orange)" stroke-width="1.6"/><path d="M6 10.3l2.6 2.5L14 7.5" fill="none" stroke="var(--orange)" stroke-width="1.8"/></svg>Power Monitoring</li>
      <li><svg viewBox="0 0 20 20"><circle cx="10" cy="10" r="8.5" fill="none" stroke="var(--orange)" stroke-width="1.6"/><path d="M6 10.3l2.6 2.5L14 7.5" fill="none" stroke="var(--orange)" stroke-width="1.8"/></svg>Safety Checks</li>
    </ul>
    <div class="photo" role="img" aria-label="Photo of an electrician in a blue hard hat and overalls fitting a ceiling light"></div>
    <svg class="band-bottom" viewBox="0 0 400 170" preserveAspectRatio="none">
      <path d="M180 70C270 50 340 20 400 0V60C330 70 260 80 180 90Z" fill="var(--blue)"/>
      <path d="M0 30C140 30 260 80 400 50V170H0Z" fill="var(--orange)"/>
      <path d="M0 30C60 30 100 50 130 70L0 170Z" fill="var(--orange-deep)"/>
    </svg>
  </section>

  <section class="panel panel-philosophy">
    <svg class="band-top" viewBox="0 0 400 90" preserveAspectRatio="none">
      <path d="M0 0H400V0C300 0 120 20 0 60Z" fill="var(--blue)"/>
      <path d="M0 60C100 30 220 14 330 10L0 40Z" fill="#b9bec4"/>
    </svg>
    <h2 class="heading"><span class="light">Our </span><span class="bold">Philosophy</span></h2>
    <div class="rule"></div>
    <p class="philosophy-text">Volta Line Electrical focuses on providing our customers with the best possible service available. Our trades people are highly qualified to ensure quality and reliability. We strive to continually change and grow within the industry. We are constantly making changes to serve you better.</p>
    <div class="photo" role="img" aria-label="Photo of hands testing a wall socket with a yellow multimeter"></div>
    <svg class="cta-block" viewBox="0 0 400 370" preserveAspectRatio="none">
      <path d="M0 120L260 0H400V370H0Z" fill="var(--blue)"/>
      <path d="M0 120L260 0H300L0 150Z" fill="var(--blue-dark)"/>
    </svg>
    <p class="cta-text">Call us today<br><span class="highlight">for a free</span><br>no obligation<br>quote</p>
    <div class="phone-pill">
      <svg viewBox="0 0 40 40"><circle cx="20" cy="20" r="17" fill="none" stroke="var(--orange)" stroke-width="3"/><path d="M14 11c1-1 2.5-1 3 0l1.6 3c.4.8.1 1.6-.5 2.1l-1 .8c.9 2.3 2.7 4.1 5 5l.8-1c.5-.6 1.3-.9 2.1-.5l3 1.6c1 .5 1 2 0 3l-1.4 1.4c-1.2 1.2-3.2 1.4-5 .6-4.5-2-8-5.5-10-10-.8-1.8-.6-3.8.6-5Z" fill="var(--orange)"/></svg>
      <span>0412570394</span>
    </div>
  </section>

  <div class="emergency">
    <span class="dot"></span>
    <span class="label">24/7 Emergency Service</span>
  </div>

</main>
</body>
</html>
```